Wine Label for a wine from Tuscany, Italy

We need a wine label for a white and red wine, can be the same label or can be somewhat differentiated with any variation you feel would be good.. These two wines come from Tuscany, Italy. Wine labels from Tuscany Italy tend to be traditional. We are open to traditional looking labels but also more modern, eye catching too. We want to convey a sense of elegance, importance, great wine. I am attaching some examples of labels we like from Tuscany, also a label that was designed for us recently by one of you, which we LOVE. No wine glasses, wine bottles or grapes featured on the label please. We tend to like the white background. No blue please.

Target Market(s)

More women than men purchase wine, but it needs to appeal to both sexes.

Requirements
Must have
• Wine Name: Casa Morel or Casa morel
• Type/Varletal: Rosso Toscano (White is Vermentino)
• Vintage (year): 2018
• That is all the text we want on the label, thanks
Nice to have
• Clean, something that makes someone want to grab this wine bottle off the shelf!
Should not have
• Images of Wine glass, wine bottles, grapes
• Do not use the color blue please.

```html
<!DOCTYPE html>
<html lang="en">
<head>
<meta charset="utf-8">
<title>Casa Morel – Wine Labels</title>
<link rel="stylesheet" href="https://fonts.googleapis.com/css2?family=Josefin+Sans:wght@400&family=EB+Garamond:wght@400&display=swap">
<style>
  :root {
    --backdrop: #0b0b0c;
    --label-paper: #ffffff;
    --label-frame: #2a2a2a;
    --ink: #1c1c1c;
    --rosso: #a3272b;
    --vermentino: #7e7a2c;
  }
  html, body {
    margin: 0;
    padding: 0;
    width: 1200px;
    height: 1000px;
    overflow: hidden;
    background: var(--backdrop);
  }
  .canvas {
    width: 1200px;
    height: 1000px;
    display: flex;
    justify-content: center;
    align-items: center;
    gap: 90px;
  }
  .label {
    position: relative;
    width: 340px;
    height: 620px;
    background: var(--label-paper);
    box-sizing: border-box;
  }
  .label__frame {
    position: absolute;
    inset: 14px;
    border: 1.5px solid var(--label-frame);
  }
  .label__name {
    position: absolute;
    top: 292px;
    left: 0;
    right: 0;
    text-align: center;
    font-family: "Josefin Sans", sans-serif;
    font-weight: 400;
    font-size: 29px;
    letter-spacing: 0.2em;
    color: var(--ink);
    text-transform: uppercase;
  }
  .label__varietal {
    position: absolute;
    top: 478px;
    left: 0;
    right: 0;
    text-align: center;
    font-family: "EB Garamond", serif;
    font-size: 17px;
    letter-spacing: 0.04em;
    text-transform: uppercase;
  }
  .label--rosso .label__varietal { color: var(--rosso); }
  .label--vermentino .label__varietal { color: var(--vermentino); }
  .label__vintage {
    position: absolute;
    top: 506px;
    left: 0;
    right: 0;
    text-align: center;
    font-family: "EB Garamond", serif;
    font-size: 17px;
    letter-spacing: 0.06em;
    color: var(--ink);
  }
</style>
</head>
<body>
  <main class="canvas">
    <section class="label label--rosso">
      <div class="label__frame"></div>
      <div class="label__name">Casa Morel</div>
      <div class="label__varietal">Rosso Toscano</div>
      <div class="label__vintage">2018</div>
    </section>
    <section class="label label--vermentino">
      <div class="label__frame"></div>
      <div class="label__name">Casa Morel</div>
      <div class="label__varietal">Vermentino</div>
      <div class="label__vintage">2018</div>
    </section>
  </main>
</body>
</html>
```